I need a business card design for a new company that will be doing consulting work around issues of cultural competency, and diversity and inclusion. I would like the design to be crisp and clear with bold but conservative colors and incorporate shades of blue

Target Market(s)

Small businesses, schools, non-profits

Industry/Entity Type

Consulting

Font styles to use
Serif
Sans Serif

Colors
0c5ba6
6b449b
3276b5
0292cd

Requirements
Must have
• A Morrow Venture (name of company)
• Tiru Morrow
• CEO
• tiru@amorrowventure.example
• (215)555-0147

```html
<!DOCTYPE html>
<html lang="en">
<head>
<meta charset="utf-8">
<title>Morrow Venture — Business Card</title>
<link rel="stylesheet" href="https://fonts.googleapis.com/css2?family=Lato:wght@400;700;900&display=swap">
<style>
  :root {
    --page: #e9e7e3;
    --paper: #eef0f5;
    --ink: #1b1b1f;
    --blue-light: #3b7ab8;
    --blue-mid: #345a96;
    --blue-deep: #2c4a86;
    --blue-ring: #2e59a8;
    --icon-blue: #3a63b5;
    --dark-1: #1f2023;
    --dark-2: #18191c;
    --dark-3: #0f1012;
    --text-light: #d9dbe0;
    --photo-grey: #bdbdc0;
  }
  * { box-sizing: border-box; margin: 0; padding: 0; }
  html, body { width: 1200px; height: 789px; overflow: hidden; background: var(--page); }
  body { font-family: "Lato", sans-serif; position: relative; }

  .card {
    position: absolute; left: 75px; top: 95px;
    width: 1050px; height: 600px;
    background: var(--paper);
    overflow: hidden;
    box-shadow: 0 18px 40px rgba(0,0,0,.25);
  }
  .card__edge {
    position: absolute; top: 0; right: 0; width: 52%; height: 9px;
    background: var(--blue-deep);
  }
  .company {
    position: absolute; left: 60px; top: 92px;
    font-size: 36px; font-weight: 700; color: var(--ink); letter-spacing: .3px;
  }
  .photo {
    position: absolute; left: 505px; top: 118px;
    width: 128px; height: 128px; border-radius: 50%;
    background: var(--photo-grey);
    border: 6px solid var(--blue-ring);
  }
  .person { position: absolute; left: 658px; top: 148px; }
  .person__name { font-size: 56px; font-weight: 900; color: var(--ink); line-height: 1; letter-spacing: .5px; }
  .person__role { font-size: 26px; font-weight: 400; color: var(--ink); text-align: center; margin-top: 2px; padding-left: 40px; }

  .columns { position: absolute; left: 0; top: 330px; width: 100%; height: 270px; display: flex; }
  .column { flex: 1; position: relative; }
  .column__band { height: 80px; }
  .column__body {
    height: 190px; display: flex; align-items: center; justify-content: center;
    text-align: center; color: var(--text-light); padding: 0 20px;
  }
  .column--phone .column__band { background: var(--blue-light); }
  .column--phone .column__body { background: var(--dark-1); }
  .column--email .column__band { background: var(--blue-mid); }
  .column--email .column__body { background: var(--dark-2); }
  .column--address .column__band { background: var(--blue-deep); }
  .column--address .column__body { background: var(--dark-3); }

  .contact-phone { font-size: 26px; letter-spacing: 1.5px; }
  .contact-email { font-size: 17px; letter-spacing: 1.2px; text-transform: uppercase; }
  .contact-address { font-size: 24px; letter-spacing: 1.5px; text-transform: uppercase; line-height: 1.1; }

  .icon-badge {
    position: absolute; top: -40px; left: 50%; margin-left: -40px;
    width: 80px; height: 80px; border-radius: 50%;
    background: #f4f5f8;
    box-shadow: 0 4px 10px rgba(0,0,0,.2);
    display: flex; align-items: center; justify-content: center;
  }
  .icon-badge svg { width: 40px; height: 40px; fill: none; stroke: var(--icon-blue); stroke-width: 2.2; stroke-linecap: round; stroke-linejoin: round; }
</style>
</head>
<body>
  <div class="card">
    <div class="card__edge"></div>
    <div class="company">Morrow Venture</div>
    <div class="photo" role="img" aria-label="Portrait photo of Tiru Morrow"></div>
    <div class="person">
      <div class="person__name">Tiru Morrow</div>
      <div class="person__role">CEO</div>
    </div>

    <div class="columns">
      <div class="column column--phone">
        <div class="column__band"></div>
        <div class="icon-badge">
          <svg viewBox="0 0 40 40" aria-hidden="true">
            <path d="M12 8l5 6-3 3c2 4 5 7 9 9l3-3 6 5-3 4c-10-1-19-10-20-20z"/>
            <path d="M24 8a9 9 0 0 1 8 8"/>
            <path d="M24 13a4 4 0 0 1 3 3"/>
          </svg>
        </div>
        <div class="column__body"><span class="contact-phone">(215)555-0147</span></div>
      </div>
      <div class="column column--email">
        <div class="column__band"></div>
        <div class="icon-badge">
          <svg viewBox="0 0 40 40" aria-hidden="true">
            <rect x="11" y="6" width="18" height="28" rx="9"/>
            <line x1="20" y1="11" x2="20" y2="17"/>
          </svg>
        </div>
        <div class="column__body"><span class="contact-email">tiru@amorrowventure.example</span></div>
      </div>
      <div class="column column--address">
        <div class="column__band"></div>
        <div class="icon-badge">
          <svg viewBox="0 0 40 40" aria-hidden="true">
            <path d="M20 35s-10-11-10-19a10 10 0 0 1 20 0c0 8-10 19-10 19z"/>
            <circle cx="20" cy="16" r="4"/>
          </svg>
        </div>
        <div class="column__body"><span class="contact-address">Put your adresse<br>here</span></div>
      </div>
    </div>
  </div>
</body>
</html>
```